Brain Science Music company needs modern clean website

We're looking for a website that's very clean and modern but also has some nice bold (futuristic) colors in it. The design should communicate a company that's providing something new and fresh! We'd greatly appreciate web designs similar to: https://thevarnishworks.co/

Lumen Cadence is a US-based Neuroscience music company that offers state-of-the-art technology solutions that help people focus, relax and sleep with the help of scientifically engineered music.

Target Market(s)

US businesses looking for specialized neuroscience music technology.

Logo Text

LumenCadence or LC

Coding

Coded - Design and coding required

Number of Pages Required

1 page

Font styles to use
Sans Serif

Colors

Designer to choose colors to be used in the design.

Requirements
Nice to have
• A website similar to: https://thevarnishworks.co/
We like the colors, the fonts, the simple design layouts and the colorful images.

```html
<!DOCTYPE html>
<html lang="en">
<head>
<meta charset="utf-8">
<title>Lumen Cadence — Neuroscience Music</title>
<link href="https://fonts.googleapis.com/css2?family=Roboto:wght@400;500;700;900&display=swap" rel="stylesheet">
<style>
:root{
  --indigo:#33069b;
  --indigo-soft:#3d12a8;
  --cyan:#13bfe2;
  --orange:#f39200;
  --violet:#7a1ea6;
  --magenta:#c2185b;
  --green:#1f9b16;
  --ink:#3a3a48;
  --paper:#f4f4f5;
  --white:#ffffff;
}
*{margin:0;padding:0;box-sizing:border-box}
html,body{width:1200px;height:3675px;overflow:hidden}
body{background:var(--paper);font-family:"Roboto",Arial,sans-serif;color:var(--ink);position:relative}
.abs{position:absolute}
.blob{position:absolute;display:block}
.accent{color:var(--cyan)}
.brand{font-weight:700;font-size:22px;color:var(--indigo);letter-spacing:-.2px}

/* header */
.site-header .brand{left:150px;top:24px}
.nav{position:absolute;top:26px;left:580px;display:flex;align-items:center;gap:0;font-size:12.5px;color:var(--white);font-weight:500}
.nav a{color:inherit;text-decoration:none;position:absolute;white-space:nowrap;top:3px}
.nav .contact{background:var(--cyan);border-radius:14px;padding:6px 18px;top:-2px}

/* hero */
.hero-title{left:150px;top:180px;font-size:50px;line-height:53px;font-weight:900;color:var(--indigo);letter-spacing:-.3px}
.hero-copy{left:150px;top:365px;width:355px;font-size:14.5px;line-height:22.5px}
.hero-art{left:610px;top:75px;width:380px;height:360px;border-radius:50%;
  background:radial-gradient(circle,rgba(44,210,240,.55),rgba(44,170,230,.15) 55%,transparent 72%)}

/* section headings */
.section-title{left:150px;font-size:38px;line-height:38px;font-weight:700;color:var(--indigo)}
.rule{position:absolute;left:150px;width:136px;height:4px;background:var(--cyan)}

/* features */
.feature{position:absolute;width:230px}
.feature h3{font-size:17.5px;font-weight:500;margin-bottom:6px}
.feature p{font-size:14.5px;line-height:22.5px}
.feature.right{text-align:right}
.chip{position:absolute;width:37px;height:37px;border-radius:7px}
.brain-art{left:500px;top:878px;width:200px;height:222px;border-radius:48% 48% 44% 44%;background:var(--cyan)}

/* entrainment */
.step-num{position:absolute;font-size:38px;font-weight:700;color:var(--indigo)}
.step-text{position:absolute;font-size:17.5px;line-height:23px}
.icon-art{position:absolute;border-radius:50%}

/* story */
.story-lead{left:148px;top:2572px;width:905px;font-size:14.5px;line-height:22.5px}
.timeline{left:592px;top:2685px;width:465px;font-size:14.5px;line-height:22.5px}
.timeline p{margin-bottom:22.5px}
.book-art{left:150px;top:2665px;width:370px;height:300px;border-radius:40% 40% 20% 20%;
  background:linear-gradient(180deg,#dfe3ff 0%,#f6ecd0 60%,#8e97f5 100%)}

/* footer */
.footer-text{color:var(--white)}
.footer-title{font-size:17.5px;font-weight:500}
.social{position:absolute;top:3505px;width:29px;height:29px;border-radius:50%;background:var(--white)}
.copyright{left:0;width:1200px;top:3632px;text-align:center;font-size:13px}
</style>
</head>
<body>

<!-- hero blob -->
<svg class="blob" style="left:520px;top:0" width="680" height="545" viewBox="0 0 680 545">
  <path d="M70 0 H680 V525 C620 545 520 545 430 520 C330 495 250 470 190 420 C120 360 40 330 40 240 C40 170 80 130 60 80 C50 40 55 15 70 0 Z" fill="var(--indigo)"/>
</svg>
<div class="abs hero-art" role="img" aria-label="Glowing network brain illustration with floating music notes"></div>

<header class="site-header">
  <div class="abs brand">LumenCadence</div>
  <nav class="nav">
    <a style="left:0">Home</a>
    <a style="left:77px">Enhancing</a>
    <a style="left:180px">Entrainment</a>
    <a style="left:290px">Elias's Story</a>
    <a class="contact" style="left:389px">Contact</a>
  </nav>
</header>

<h1 class="abs hero-title">The new <span class="accent">FRONTIER</span><br>of <span class="accent">MUSIC</span> and<br>the <span class="accent">BRAIN</span></h1>
<p class="abs hero-copy">Lorem ipsum dolor sit amet, consectetur adipiscing elit. Aenean ante eros, ullamcorper quis dignissim eget, volutpat</p>

<!-- enhancing -->
<h2 class="abs section-title" style="top:720px">Merging <span class="accent">Neuroscience</span> and <span class="accent">Music</span>,<br>Creating audio <span class="accent">Enhancing</span></h2>
<div class="rule" style="top:818px"></div>

<svg class="blob" style="left:195px;top:880px" width="810" height="135" viewBox="0 0 810 135">
  <polyline points="0,22 230,22 280,75" fill="none" stroke="var(--orange)" stroke-width="1.2"/>
  <polyline points="0,132 230,132 280,77" fill="none" stroke="var(--violet)" stroke-width="1.2"/>
  <circle cx="281" cy="76" r="3" fill="var(--indigo)"/>
  <polyline points="800,22 565,22 520,74" fill="none" stroke="var(--magenta)" stroke-width="1.2"/>
  <polyline points="800,132 568,132 520,76" fill="none" stroke="var(--green)" stroke-width="1.2"/>
  <circle cx="520" cy="75" r="3" fill="var(--indigo)"/>
</svg>

<div class="chip" style="left:150px;top:880px;background:var(--orange)"></div>
<div class="feature" style="left:198px;top:875px"><h3 style="color:var(--orange)">Productivity</h3><p>Vivamus tincidunt nulla nec male-suada accumsan. Fusce lacinia, sapien ac</p></div>
<div class="chip" style="left:150px;top:988px;background:var(--violet)"></div>
<div class="feature" style="left:198px;top:985px"><h3 style="color:var(--violet)">Sleep</h3><p>Vivamus tincidunt nulla nec male-suada accumsan. Fusce lacinia, sapien ac</p></div>

<div class="abs brain-art" role="img" aria-label="Bold cyan brain illustration"></div>

<div class="chip" style="left:1012px;top:878px;background:var(--magenta)"></div>
<div class="feature right" style="left:765px;top:874px"><h3 style="color:var(--magenta)">Meditation</h3><p>Vivamus tincidunt nulla nec male-suada accumsan. Fusce lacinia, sapien ac</p></div>
<div class="chip" style="left:1012px;top:988px;background:var(--green)"></div>
<div class="feature right" style="left:765px;top:985px"><h3 style="color:var(--green)">Athletics</h3><p>Vivamus tincidunt nulla nec male-suada accumsan. Fusce lacinia, sapien ac</p></div>

<!-- entrainment -->
<h2 class="abs section-title" style="top:1278px">Brainwave <span class="accent">Entrainment</span></h2>
<div class="rule" style="top:1334px"></div>

<svg class="blob" style="left:0;top:1393px" width="310" height="345" viewBox="0 0 310 345">
  <path d="M0 15 C60 0 150 -5 220 20 C290 50 310 120 305 190 C300 270 250 320 170 335 C110 345 50 340 0 340 Z" fill="var(--indigo)"/>
</svg>
<div class="icon-art" style="left:210px;top:1460px;width:140px;height:150px;background:linear-gradient(90deg,var(--orange) 55%,var(--cyan))" role="img" aria-label="Half brain with circuit connectors"></div>
<div class="step-num" style="left:428px;top:1470px">01</div>
<p class="step-text" style="left:430px;top:1525px;width:580px;color:var(--orange)">Neurons in our brains communicate with each other, forming thoughts, emotions, and ideas using electrical impulses (commonly known as Brainwaves).</p>

<svg class="blob" style="left:850px;top:1578px" width="350" height="335" viewBox="0 0 350 335">
  <path d="M350 10 C290 0 200 -5 130 30 C50 70 10 140 5 200 C0 270 50 325 140 330 C220 335 290 325 350 330 Z" fill="var(--indigo)"/>
</svg>
<div class="icon-art" style="left:808px;top:1695px;width:130px;height:130px;background:linear-gradient(90deg,var(--violet) 50%,var(--orange) 50%)" role="img" aria-label="Two-tone lightbulb brain with rays"></div>
<div class="step-num" style="left:676px;top:1688px">02</div>
<p class="step-text" style="left:150px;top:1742px;width:566px;text-align:right;color:var(--violet)">Activities such as sleeping, working, or meditating, each have their own unique brainwave pattern.</p>

<svg class="blob" style="left:0;top:1825px" width="310" height="348" viewBox="0 0 310 348">
  <path d="M0 20 C60 0 150 -5 220 30 C290 70 310 140 302 210 C295 280 240 320 160 335 C100 345 40 345 0 345 Z" fill="var(--indigo)"/>
</svg>
<div class="icon-art" style="left:188px;top:1895px;width:152px;height:130px;background:linear-gradient(90deg,var(--magenta) 50%,#1c5f7a 50%)" role="img" aria-label="Two brain halves with circuit nodes"></div>
<div class="step-num" style="left:428px;top:1898px">03</div>
<p class="step-text" style="left:430px;top:1953px;width:580px;color:var(--magenta)">Lumen Cadence leverages Musical Phase Locking, to optimize brainwave patterns for each desired activity.</p>

<svg class="blob" style="left:850px;top:2023px" width="350" height="322" viewBox="0 0 350 322">
  <path d="M350 5 C290 -5 200 0 130 35 C50 75 10 140 5 200 C0 265 50 315 140 318 C220 322 290 312 350 318 Z" fill="var(--indigo)"/>
</svg>
<div class="icon-art" style="left:790px;top:2105px;width:170px;height:140px;background:radial-gradient(circle,var(--green) 30%,#f7f1c8 36%,#f7f1c8 40%,rgba(255,255,255,0) 42%)" role="img" aria-label="Brain in a circle with coloured connector nodes"></div>
<div class="step-num" style="left:676px;top:2100px">04</div>
<p class="step-text" style="left:150px;top:2155px;width:566px;text-align:right;color:var(--green)">Our music is driven by science. We utilize large scale studies<br>and data &nbsp;from electroencephlograms to produce<br>substantial results.</p>

<!-- story -->
<h2 class="abs section-title" style="top:2472px">Elias’s <span class="accent">Story</span></h2>
<div class="rule" style="top:2528px"></div>
<p class="abs story-lead">Founder and Team Leader of Lumen Cadence, in conjunction with &nbsp;primary scientific advisor Dr. Harlan Voss. Elias is a pioneer in the neuroscience of music, and key innovator on the technology of Musical Phase Locking.</p>

<svg class="blob" style="left:0;top:2660px" width="350" height="498" viewBox="0 0 350 498">
  <path d="M0 30 C80 0 200 -5 270 60 C340 130 355 260 340 360 C320 450 250 498 170 496 C100 494 40 480 0 470 Z" fill="var(--indigo)"/>
</svg>
<div class="abs book-art" role="img" aria-label="Open book with floating books, pencils and music symbols"></div>

<div class="abs" style="left:905px;top:2667px;width:135px;height:1px;background:var(--cyan)"></div>
<div class="abs" style="left:564px;top:2950px;width:1px;height:140px;background:var(--cyan)"></div>
<div class="abs timeline">
  <p>At the age of 10, Elias wrote his first symphony and began studying music composition</p>
  <p>After exposure to alpha waves in music, Elias began a lifelong pursuit of merging neuroscience and music composition</p>
  <p>Elias founded Clearfield Labs in 2003, creating audio workstations for those who wanted to experience the effects of music guided by neuroscience, as well as software for brain-computer interfaces.</p>
  <p>As the science progressed and Clearfield Labs grew, Elias decided to form Mindwave.io in 2014, a website and app that allowed nearly anybody to access the music, not just those who were scientifically minded</p>
  <p>Lumen Cadence was formed to further the vision of neuroscience-based music becoming a daily resource that everyone should experience.</p>
</div>

<!-- footer -->
<svg class="blob" style="left:0;top:3318px" width="1200" height="357" viewBox="0 0 1200 357">
  <path d="M0 0 C100 5 160 30 220 40 C400 60 600 20 800 30 C950 40 1100 60 1200 70 V357 H0 Z" fill="var(--cyan)"/>
  <path d="M0 60 C120 40 220 20 380 5 C560 -5 700 30 860 30 C1000 30 1100 60 1200 80 V357 H0 Z" fill="var(--indigo)"/>
</svg>
<footer>
  <div class="abs brand footer-text" style="left:150px;top:3470px">LumenCadence</div>
  <div class="abs footer-text footer-title" style="left:382px;top:3472px">About us</div>
  <p class="abs footer-text" style="left:382px;top:3497px;width:450px;font-size:12.5px;line-height:22.5px">massa dolor, finibus non cursus dapibus, ultrices a nisl. Cras maximus bibendum eros, non rutrum arcu bibendum nec. Etiam quis orci leo. Class aptent taciti sociosqu ad litora torquent per conubia</p>
  <div class="abs footer-text footer-title" style="left:885px;top:3472px">About us</div>
  <span class="social" style="left:885px"></span>
  <span class="social" style="left:930px"></span>
  <span class="social" style="left:975px"></span>
  <span class="social" style="left:1021px"></span>
  <div class="abs" style="left:150px;top:3600px;width:900px;height:1px;background:var(--white)"></div>
  <div class="abs footer-text copyright">© &nbsp;All CopyRights are resereved</div>
</footer>

</body>
</html>
```